Talvor Visit cards serious but not sad

Hello, I'd like to design my visit cards with the logo Talvor (attached) the following information: Name: Karim Belmadi Title: Mobile Director: 33 (0) 6 72 18 35 09 Phone: 33 (0) 4 58 61 07 92 e-mail: karim.belmadi@talvor-consulting.example address: 17 Rue Marcel Danvin 92400 Courbevoie This visit will be used on the banking institutions and Talvor is a consulting firm. I do not want to have dark background.

Target Market(s)

banks

Contact Information for Business Card

Name : Karim Belmadi
Title : Director
mobile : +33(0)6 72 18 35 09
Phone : +33(0)4 58 61 07 92
e-mail: karim.belmadi@talvor-consulting.example
adresse : 17 Rue marcel Danvin 92400 Courbevoie

Requirements
Nice to have
• serious but not sad

```html
<!DOCTYPE html>
<html lang="fr">
<head>
<meta charset="utf-8">
<title>Talvor – cartes de visite</title>
<link href="https://fonts.googleapis.com/css2?family=Roboto+Condensed:wght@400;700&display=swap" rel="stylesheet">
<style>
:root{
  --stage:#2b2b2b;
  --card-white:#f7f7f7;
  --card-grey:#b1b1b1;
  --brand-blue:#1d7cc8;
  --ink:#3a3a3a;
  --muted:#9a9a9a;
  --rule:#c4c4c4;
}
*{margin:0;padding:0;box-sizing:border-box}
html,body{width:1200px;height:911px;overflow:hidden}
body{
  background:var(--stage);
  font-family:"Roboto Condensed",Arial,sans-serif;
  display:flex;flex-direction:column;align-items:center;justify-content:center;gap:60px;
}
.card{width:600px;height:343px;position:relative;box-shadow:0 6px 18px rgba(0,0,0,.35)}
.card--front{background:var(--card-white)}
.card--back{background:var(--card-grey)}

.brand{display:flex;align-items:center;gap:12px;color:var(--brand-blue);font-weight:700}
.brand__dot{border-radius:50%;background:var(--brand-blue)}

.card--front .brand{position:absolute;left:44px;top:52px;font-size:52px;line-height:1}
.card--front .brand__dot{width:52px;height:52px}
.address{position:absolute;right:44px;top:64px;text-align:right;color:var(--ink);font-size:17px;line-height:1.3}
.divider{position:absolute;left:44px;right:44px;top:148px;height:1px;background:var(--rule)}

.identity{position:absolute;left:44px;top:172px}
.identity__tab{position:absolute;left:-44px;top:3px;width:26px;height:22px;background:var(--brand-blue)}
.identity__name{color:var(--brand-blue);font-weight:700;font-size:24px;text-transform:uppercase;line-height:1.1}
.identity__title{color:var(--muted);font-size:17px;text-transform:uppercase;padding-bottom:6px;border-bottom:1px solid var(--rule);width:160px}

.contacts{list-style:none;position:absolute;left:44px;top:240px;color:var(--ink);font-size:15px;line-height:1}
.contacts li{display:flex;align-items:center;gap:10px;margin-bottom:6px}
.contacts svg{width:12px;height:12px;fill:var(--brand-blue);flex:none}

.card--back .brand{position:absolute;left:50%;top:50%;transform:translate(-50%,-50%);font-size:78px;line-height:1}
.card--back .brand__dot{width:78px;height:78px}
.website{position:absolute;left:0;right:0;top:40px;text-align:center;color:#5a5a5a;font-size:15px;letter-spacing:.35em}
</style>
</head>
<body>

<section class="card card--front" aria-label="Recto">
  <div class="brand"><span class="brand__dot"></span><span class="brand__name">Talvor</span></div>
  <p class="address">17 Rue marcel Danvin<br>92870 Valmoreuil</p>
  <div class="divider"></div>

  <div class="identity">
    <span class="identity__tab"></span>
    <p class="identity__name">Karim Belmadi</p>
    <p class="identity__title">Director</p>
  </div>

  <ul class="contacts">
    <li><svg viewBox="0 0 12 12" aria-hidden="true"><path d="M2.5 0.5l2 2.5-1.2 1.2c.6 1.5 1.9 2.8 3.5 3.5l1.2-1.2 2.5 2-1.3 2.3C4.5 10.3 1.7 7.5.5 2.3z"/></svg>+33(0)4 58 61 07 92</li>
    <li><svg viewBox="0 0 12 12" aria-hidden="true"><path d="M3 0h6a1 1 0 0 1 1 1v10a1 1 0 0 1-1 1H3a1 1 0 0 1-1-1V1a1 1 0 0 1 1-1zm0 1.5v8h6v-8z"/></svg>+33(0)6 72 18 35 09</li>
    <li><svg viewBox="0 0 12 12" aria-hidden="true"><path d="M0 2h12v8H0zm1.2 1L6 6.5 10.8 3z"/></svg>karim.belmadi@talvor-consulting.example</li>
    <li><svg viewBox="0 0 12 12" aria-hidden="true"><circle cx="6" cy="6" r="6"/><path d="M1 6h10M6 0.5v11" stroke="#f7f7f7" stroke-width="1"/></svg>www.talvor-consulting.example</li>
  </ul>
</section>

<section class="card card--back" aria-label="Verso">
  <p class="website">www.talvor-consulting.example</p>
  <div class="brand"><span class="brand__dot"></span><span class="brand__name">Talvor</span></div>
</section>

</body>
</html>
```